US Based Startup requires Website Design for Velmora Cell

We are launching a battery technology called "Velmora Cell" for which we need an elegant website design. We use red and black to represent positive and negative node color used in battery. The background is white. The font must provide more wide space and easy to read.
Velmora CellTM is a technology that uses fast switches, such as transistor switches, to make batteries more efficient. The novel technology can be implemented in all types of batteries – including non-rechargeable batteries, rechargeable batteries, wet-cell batteries and all metal oxide batteries.
Normal batteries are “non-switching”, that is, these batteries can only be connected to one another in parallel or series connections. Parallel connections enable batteries to charge faster whilst series connections enable the battery to discharge more efficiently to the load.
Velmora CellTM technology enables batteries to be connected in a third connection method called “duo-braidTM” that combines the benefit of faster charging of the batteries with renewable energy source, such as solar, in parallel connection, and then quickly re-configures the same batteries using the fast transistor switches, to be connected in series with the load, to discharge efficiently.

Target Market(s)

Renewable energy

Industry/Entity Type

Renewable

Coding

Coded - Design and coding required

Number of Pages Required

5+ page

Requirements
Must have
• The primary colors are red and black for logo and fonts. The background is white.
The font must be easy to read type of fonts with more white space. Only pictures will be in full color.
Nice to have
• Elegant and simple design bringing out a new battery concept to the energy industry.

```html
<!DOCTYPE html>
<html lang="en">
<head>
<meta charset="utf-8">
<title>Velmora Cell</title>
<link rel="stylesheet" href="https://fonts.googleapis.com/css2?family=Oswald:wght@500;600&family=Poppins:wght@400;500;600&display=swap">
<style>
:root{
  --red:#e31b1b;
  --red-deep:#c8102e;
  --black:#111111;
  --dark:#1e1e1e;
  --text:#222222;
  --muted:#555555;
  --grey:#f1f1f3;
  --star:#f5b800;
  --white:#ffffff;
}
*{margin:0;padding:0;box-sizing:border-box}
html,body{width:1200px;height:4044px;overflow:hidden;background:var(--white)}
body{position:relative;font-family:"Poppins",sans-serif;color:var(--text)}
.abs{position:absolute}
.display{font-family:"Oswald",sans-serif;font-weight:600;text-transform:uppercase;color:var(--black);letter-spacing:-.3px}
.btn{position:absolute;display:flex;align-items:center;justify-content:center;background:var(--red);color:#fff;font-family:"Poppins",sans-serif;font-weight:600;font-size:12px;text-transform:uppercase;letter-spacing:.3px}

/* header */
.brand{left:87px;top:22px;font-family:"Oswald",sans-serif;font-weight:600;font-size:22px;text-transform:uppercase;color:var(--black)}
.brand sup{font-size:10px;color:#999;font-weight:500}
.nav{left:512px;top:27px;display:flex;gap:14px;font-family:"Oswald",sans-serif;font-weight:500;font-size:14px;text-transform:uppercase;color:var(--black)}
.nav-icons{left:1015px;top:22px;display:flex;gap:12px}
.cart-badge{position:absolute;right:-6px;top:-4px;width:12px;height:12px;border-radius:50%;background:var(--red);color:#fff;font-size:8px;display:flex;align-items:center;justify-content:center}

/* hero */
.hero-title{left:88px;top:248px;font-size:62px;line-height:58px}
.hero-title .accent{color:var(--red)}
.hero-text{left:88px;top:435px;width:480px;font-size:15px;line-height:23px;color:var(--muted)}
.hero-product{left:648px;top:145px;width:418px;height:475px;border-radius:14px;background:linear-gradient(180deg,#2a2a2a,#0d0d0d 60%,#1a1a1a)}

/* advantages */
.adv-title{left:0;width:1200px;top:795px;text-align:center;font-size:44px;color:#fff}
.adv{position:absolute;top:895px;width:230px;text-align:center;color:#fff}
.adv h3{font-family:"Oswald",sans-serif;font-weight:500;font-size:17px;text-transform:uppercase;margin-top:20px}
.adv p{font-size:13px;line-height:20px;margin-top:10px;color:#e8e8e8}

/* products */
.sec-title{left:0;width:1200px;text-align:center;font-size:44px}
.card{position:absolute;top:1330px;width:243px;height:318px;background:#fff;box-shadow:0 6px 22px rgba(0,0,0,.1);text-align:center}
.card .photo{position:absolute;left:35px;top:55px;width:173px;height:120px;border-radius:6px}
.stars{color:var(--star);font-size:14px;letter-spacing:4px}
.card h4{font-family:"Oswald",sans-serif;font-weight:500;font-size:16px;text-transform:uppercase;color:var(--black);margin-top:6px}
.price{font-weight:600;font-size:17px;color:#888;margin-top:6px}
.card .info{position:absolute;left:0;width:100%;top:212px}

/* about */
.about-photo{left:0;top:1737px;width:552px;height:418px}
.about-title{left:635px;top:1805px;font-size:42px;line-height:46px}
.about-text{left:635px;top:1908px;width:460px;font-size:15px;line-height:24px;color:var(--muted)}

/* video band */
.band{left:0;top:2218px;width:1200px;height:430px;background:linear-gradient(90deg,#c4151c,#e0262a 50%,#c4151c)}
.band-title{left:0;width:1200px;top:2355px;text-align:center;font-size:42px;color:#fff}
.band-text{left:0;width:1200px;top:2417px;text-align:center;font-size:15px;line-height:24px;color:#fff}
.play{left:564px;top:2469px;width:72px;height:72px;border-radius:50%;background:#fff}

/* blog */
.post{position:absolute;top:2800px;width:329px;height:405px;background:#fff;box-shadow:0 6px 22px rgba(0,0,0,.1)}
.post .photo{height:195px;background:linear-gradient(135deg,#5c6670,#2f3a44 55%,#8a5b3b)}
.post .body{padding:22px 28px 0 36px}
.post h4{font-family:"Oswald",sans-serif;font-weight:500;font-size:20px;text-transform:uppercase;color:var(--black)}
.post p{font-size:13px;line-height:19px;color:#333;margin-top:6px}
.post a{display:block;margin-top:8px;font-family:"Oswald",sans-serif;font-weight:500;font-size:15px;color:var(--red);text-transform:uppercase;text-decoration:none}

/* mailing */
.mail-field{left:355px;top:3367px;width:345px;height:49px;background:var(--black);color:#fff;font-size:15px;display:flex;align-items:center;gap:8px;padding-left:22px}
.mail-btn{left:700px;top:3367px;width:145px;height:49px;font-size:16px}

/* footer */
.foot-brand{left:126px;top:3795px;font-family:"Oswald",sans-serif;font-weight:600;font-size:38px;text-transform:uppercase;color:var(--black)}
.foot-brand sup{font-size:16px}
.socials{left:192px;top:3853px;display:flex;gap:8px}
.socials span{width:34px;height:34px;border-radius:50%;background:#e2e2e6;display:block}
.foot-col{position:absolute;top:3730px}
.foot-col h5{font-family:"Oswald",sans-serif;font-weight:500;font-size:18px;text-transform:uppercase;color:var(--black);margin-bottom:14px}
.foot-col li{list-style:none;font-size:14px;color:#444;line-height:28.5px}
.contact-row{display:flex;gap:9px;font-size:13.5px;line-height:18px;color:#444;margin-bottom:18px}
.contact-row svg{flex:none;margin-top:2px}
.rule{left:90px;top:3990px;width:1020px;height:1px;background:#cfcfd4}
.copy{left:0;width:1200px;top:4016px;text-align:center;font-size:11px;color:#222;text-transform:uppercase}
.to-top{left:1134px;top:3978px;width:40px;height:40px;border-radius:50%;background:var(--red)}
</style>
</head>
<body>

<!-- header -->
<div class="abs brand">Velmora Cell <sup>TM</sup></div>
<nav class="abs nav"><span>Home</span><span>About Us</span><span>Products</span><span>Features</span><span>Brands</span><span>Sponsorship</span><span>Contact Us</span></nav>
<div class="abs nav-icons">
  <svg width="20" height="22" viewBox="0 0 20 22" fill="none" stroke="#111" stroke-width="1.6"><circle cx="10" cy="7" r="5"/><path d="M2 21c0-5 3.5-8 8-8s8 3 8 8"/></svg>
  <svg width="20" height="22" viewBox="0 0 20 22" fill="none" stroke="#111" stroke-width="1.6"><circle cx="8.5" cy="9" r="6"/><path d="M13 13.5l5 5"/></svg>
  <span style="position:relative;display:block">
    <svg width="22" height="22" viewBox="0 0 22 22" fill="none" stroke="#111" stroke-width="1.6"><path d="M1 3h3l3 11h11l2-8H6"/><circle cx="8" cy="19" r="1.5"/><circle cx="17" cy="19" r="1.5"/></svg>
    <span class="cart-badge">0</span>
  </span>
</div>

<!-- hero / advantages background -->
<svg class="abs" style="left:0;top:440px" width="1200" height="733" viewBox="0 0 1200 733">
  <polygon points="0,360 1200,30 1200,733 0,733" fill="var(--dark)"/>
  <polygon points="0,350 1200,22 1200,40 0,372" fill="var(--dark)"/>
  <polygon points="0,330 630,148 518,200 0,355" fill="var(--red)"/>
  <polygon points="518,200 630,148 560,258 0,380 0,355" fill="var(--red)"/>
  <polygon points="0,380 560,258 600,252 0,392" fill="var(--dark)"/>
</svg>

<h1 class="abs display hero-title">Revolutionary<br><span class="accent">Battery Switching</span><br>Technology</h1>
<p class="abs hero-text">Aenean sollicitudin lorem quis bibendum auctor quat ipsum, nec sagittis sem nibh id elit duis sed odio...</p>
<div class="btn" style="left:88px;top:492px;width:138px;height:43px">Get Started</div>
<div class="abs hero-product" role="img" aria-label="Black car battery with red and black terminals and a blue product label"></div>

<!-- advantages -->
<h2 class="abs display adv-title">Advantages</h2>
<div class="adv" style="left:81px">
  <svg width="100" height="72" viewBox="0 0 100 72"><rect x="8" y="30" width="16" height="5" fill="var(--red)"/><rect x="4" y="40" width="20" height="5" fill="var(--red)"/><rect x="12" y="50" width="12" height="5" fill="var(--red)"/><circle cx="56" cy="42" r="27" fill="#fff"/><circle cx="56" cy="42" r="20" fill="#111"/><circle cx="56" cy="42" r="3" fill="var(--red)"/><path d="M56 42l10-10" stroke="var(--red)" stroke-width="3"/><rect x="49" y="4" width="14" height="8" fill="#fff"/></svg>
  <h3>Under 3 Minutes</h3><p>Lorem Ipsum is simply dummy text of the printing and typeset-ting industry.</p>
</div>
<div class="adv" style="left:358px">
  <svg width="100" height="72" viewBox="0 0 100 72"><path d="M30 8c0 10 8 14 8 26v20a6 6 0 0 0 12 0V30" fill="none" stroke="#fff" stroke-width="3"/><rect x="50" y="6" width="30" height="62" rx="3" fill="#fff"/><rect x="56" y="14" width="18" height="24" fill="var(--red)"/><rect x="50" y="60" width="30" height="8" fill="var(--red)"/></svg>
  <h3>Drive-Thru</h3><p>Lorem Ipsum is simply dummy text of the printing and typeset-ting industry.</p>
</div>
<div class="adv" style="left:626px">
  <svg width="100" height="72" viewBox="0 0 100 72"><ellipse cx="50" cy="58" rx="30" ry="9" fill="none" stroke="var(--red)" stroke-width="4"/><path d="M50 62c-10-14-20-24-20-36a20 20 0 0 1 40 0c0 12-10 22-20 36z" fill="#fff"/><circle cx="50" cy="26" r="8" fill="#111"/></svg>
  <h3>Infrastructure</h3><p>Lorem Ipsum is simply dummy text of the printing and typeset-ting industry.</p>
</div>
<div class="adv" style="left:895px">
  <svg width="100" height="72" viewBox="0 0 100 72"><rect x="22" y="30" width="20" height="36" fill="var(--red)"/><path d="M44 32l12-24c6 0 8 4 7 10l-2 10h16c5 0 7 4 6 8l-5 24c-1 4-4 6-8 6H44z" fill="#fff"/></svg>
  <h3>Reduced Prices</h3><p>Lorem Ipsum is simply dummy text of the printing and typeset-ting industry.</p>
</div>

<!-- products -->
<h2 class="abs display sec-title" style="top:1255px">Our Products</h2>
<div class="card" style="left:90px">
  <div class="photo" role="img" aria-label="Grey deep-cycle battery" style="background:linear-gradient(180deg,#4a4a4a 0 22%,#d9dadc 22%)"></div>
  <div class="info" style="top:212px"><div class="stars">★★★★★</div><h4>Product Heading Goes Here</h4><div class="price">€25.00</div></div>
</div>
<div class="card" style="left:349px">
  <div class="photo" role="img" aria-label="White inverter battery with red label" style="background:linear-gradient(180deg,#e8e8ea 0 30%,#c8102e 30% 75%,#efefef 75%)"></div>
  <div class="info" style="top:212px"><div class="stars">★★★★★</div><h4>Product Heading Goes Here</h4><div class="price">€25.00</div></div>
</div>
<div class="card" style="left:607px">
  <div class="photo" role="img" aria-label="White and black tubular battery" style="left:73px;top:55px;width:97px;height:95px;background:linear-gradient(180deg,#222 0 20%,#ececec 20% 55%,#c8102e 55% 75%,#ececec 75%)"></div>
  <div class="info" style="top:172px"><div class="stars">★★★★★</div><h4>Product Heading Goes Here</h4><div class="price">€25.00</div>
    <div class="btn" style="position:relative;margin:10px auto 0;width:162px;height:34px">Add to Cart</div></div>
</div>
<div class="card" style="left:868px">
  <div class="photo" role="img" aria-label="Dark blue car battery" style="background:linear-gradient(180deg,#2a2f3a 0 25%,#3c4a6a 25% 80%,#222 80%)"></div>
  <div class="info" style="top:212px"><div class="stars">★★★★★</div><h4>Product Heading Goes Here</h4><div class="price">€25.00</div></div>
</div>

<!-- about -->
<svg class="abs about-photo" viewBox="0 0 552 418" role="img" aria-label="Technician connecting a red battery charger inside a car engine bay">
  <defs><linearGradient id="engine" x1="0" y1="0" x2="1" y2="1"><stop offset="0" stop-color="#3a4350"/><stop offset=".5" stop-color="#b3242a"/><stop offset="1" stop-color="#1d2228"/></linearGradient></defs>
  <polygon points="0,0 520,0 420,418 0,418" fill="url(#engine)"/>
  <polygon points="520,0 552,0 465,200 438,215 470,210 420,418 410,418 452,228 418,238" fill="var(--red)"/>
</svg>
<h2 class="abs display about-title">About Velmora<br>Cell</h2>
<p class="abs about-text">Velmora CellTM is a technology that uses fast switches, such as transistor switches, to make batteries more efficient. The novel technology can be implemented in all types of batteries – including non-rechargeable batteries, rechargeable batteries, wet-cell batteries and all metal oxide batteries.</p>
<div class="btn" style="left:635px;top:2062px;width:137px;height:36px">Find Out More</div>

<!-- video band -->
<div class="abs band" role="img" aria-label="Red-tinted photo of a technician testing a battery with a multimeter"></div>
<h2 class="abs display band-title">The Velmora Cell</h2>
<p class="abs band-text">Aenean sollicitudin lorem quis bibendum auctor quat ipsum,<br>nec sagittis sem nibh id elit duis sed odio...</p>
<div class="abs play"><svg width="72" height="72" viewBox="0 0 72 72"><path d="M30 25l17 11-17 11z" fill="#111"/></svg></div>

<!-- blog -->
<h2 class="abs display sec-title" style="top:2730px">Latest Blog</h2>
<article class="post" style="left:88px">
  <div class="photo" role="img" aria-label="Mechanic with a wrench working on a car battery"></div>
  <div class="body"><h4>Blog Heading Here</h4><p>Lorem Ipsum is simply dummy text of the printing and typesetting industry. Lorem Ipsum has been the industry's standard dummy text ever since the 1500s, when an unknown .</p><a>Read More</a></div>
</article>
<article class="post" style="left:433px">
  <div class="photo" role="img" aria-label="Technician checking pressure gauges in an engine bay" style="background:linear-gradient(135deg,#8d96a0,#3e4650 60%,#b52a2a)"></div>
  <div class="body"><h4>Blog Heading Here</h4><p>Lorem Ipsum is simply dummy text of the printing and typesetting industry. Lorem Ipsum has been the industry's standard dummy text ever since the 1500s, when an unknown .</p><a>Read More</a></div>
</article>
<article class="post" style="left:781px">
  <div class="photo" role="img" aria-label="Hands attaching jumper clamps to a car battery" style="background:linear-gradient(135deg,#6b737c,#2a3038 55%,#c05a2a)"></div>
  <div class="body"><h4>Blog Heading Here</h4><p>Lorem Ipsum is simply dummy text of the printing and typesetting industry. Lorem Ipsum has been the industry's standard dummy text ever since the 1500s, when an unknown .</p><a>Read More</a></div>
</article>

<!-- mailing list + footer background -->
<svg class="abs" style="left:0;top:3400px" width="1200" height="644" viewBox="0 0 1200 644">
  <polygon points="0,314 1200,20 1200,644 0,644" fill="var(--grey)"/>
  <polygon points="500,200 1200,20 1200,40 640,330" fill="#f7f7f9"/>
</svg>
<h2 class="abs display sec-title" style="top:3300px">Join Our Mailing List</h2>
<div class="abs mail-field"><svg width="16" height="12" viewBox="0 0 16 12"><rect width="16" height="12" rx="1" fill="#fff"/><path d="M0 1l8 6 8-6" fill="none" stroke="#111" stroke-width="1.4"/></svg>Enter your email address</div>
<div class="btn mail-btn">Subscribe</div>

<div class="abs foot-brand">Velmora Cell <sup>TM</sup></div>
<div class="abs socials" aria-label="Social links"><span></span><span></span><span></span><span></span></div>

<div class="foot-col" style="left:508px"><h5>Quick Links</h5><ul><li>About Us</li><li>Products</li><li>Features</li><li>Brands</li><li>Sponsorship</li><li>Contact Us</li></ul></div>
<div class="foot-col" style="left:697px"><h5>Information</h5><ul><li>Privacy Policy</li><li>Return Policy</li><li>Terms &amp; Condition</li><li>Contact us</li><li>FAQ's</li></ul></div>
<div class="foot-col" style="left:893px"><h5>Contact Us</h5>
  <div class="contact-row"><svg width="13" height="10" viewBox="0 0 13 10"><rect width="13" height="10" fill="var(--red)"/><path d="M0 1l6.5 5L13 1" fill="none" stroke="#fff" stroke-width="1.2"/></svg><div>Email:<br>hello@velmoracell.example</div></div>
  <div class="contact-row"><svg width="13" height="13" viewBox="0 0 13 13"><path d="M2 1l3 0 1 3-2 1.5a8 8 0 0 0 3.5 3.5L9 7l3 1v3c0 1-1 1.5-2 1.5C5 12 1 8 .5 3 .5 2 1 1 2 1z" fill="var(--red)"/></svg><div>Phone:<br>(555) 014-2290</div></div>
  <div class="contact-row"><svg width="13" height="15" viewBox="0 0 13 15"><path d="M6.5 15C3 10 0 8 0 5.5a6.5 6.5 0 0 1 13 0C13 8 10 10 6.5 15z" fill="var(--red)"/><circle cx="6.5" cy="5.5" r="2.2" fill="#fff"/></svg><div>Office Location:<br>Some address line goes<br>here with city...</div></div>
</div>

<div class="abs rule"></div>
<div class="abs copy">© Copyright Velmora CellTM 2021. All Rights Reserved</div>
<div class="abs to-top"><svg width="40" height="40" viewBox="0 0 40 40"><path d="M20 27V14M15 19l5-5 5 5" fill="none" stroke="#fff" stroke-width="1.6"/></svg></div>

</body>
</html>
```